Kito Rise and Glow Dance Fitness-KRGDF

Catchy POSTER .
The poster must attract both eyes of all ages looking for fitness,Ritmoflex to have fun, professional dance training and Yoga.

Target Market(s)

Dancers and Non Dancers

Industry/Entity Type

Training

Requirements
Must have
• Kito Dance Ensemble
Presents
KITO RISE AND GLOW DANCE FITNESS

African Dance
Modern/Samtidsdans,
Yoga
Ritmoflex
Hip Hop
Massage and repertoire classes.

Venue:Vetlefjord Kulturhus
Call 47351208 to register/TEXT
kitoarts@kitomail.example
www.kitoarts-example.org
Nice to have
• OG creativity...think outside the box
Should not have
• Please NO cartoon charectors!!! or BALLET DANCING LIONS!!!

```html
<!DOCTYPE html>
<html lang="en">
<head>
<meta charset="utf-8">
<title>Kito Rise and Glow Dance Fitness</title>
<link rel="stylesheet" href="https://fonts.googleapis.com/css2?family=Alfa+Slab+One&family=Anton&family=Oswald:wght@300;400;500;700&family=Black+Ops+One&display=swap">
<style>
  :root {
    --paper: #eef0f3;
    --paper-edge: #d9dde3;
    --red: #c4161c;
    --red-dark: #8e0c10;
    --ink: #1c1c22;
    --slate: #3b3e48;
    --white: #ffffff;
    --yellow: #ffd21f;
    --orange: #f39a12;
    --photo-cool: #9fb3cf;
    --photo-deep: #4a5f86;
  }
  * { margin: 0; padding: 0; box-sizing: border-box; }
  html, body { width: 846px; height: 1200px; overflow: hidden; background: var(--paper); }
  .poster {
    position: relative; width: 846px; height: 1200px; overflow: hidden;
    background: radial-gradient(ellipse at 55% 40%, #ffffff 0%, var(--paper) 55%, var(--paper-edge) 100%);
    font-family: "Oswald", sans-serif;
  }
  .art { position: absolute; }
  .art--globe {
    left: 380px; top: 150px; width: 500px; height: 560px; border-radius: 50%;
    background: radial-gradient(circle at 40% 35%, #d8c9b8 0%, #9a8472 45%, #5d4a3e 75%, rgba(93,74,62,0) 76%);
    opacity: .8;
  }
  .art--dancer {
    left: 0; top: 0; width: 350px; height: 950px;
    background: linear-gradient(180deg, rgba(255,255,255,.2) 0%, var(--photo-cool) 30%, var(--photo-deep) 70%, rgba(74,95,134,.15) 100%);
    border-radius: 40% 45% 20% 30% / 12% 10% 8% 10%;
  }
  .art--speaker {
    left: 140px; top: 845px; width: 270px; height: 270px; border-radius: 50%;
    background: radial-gradient(circle, #222 0%, #3a3a3a 40%, #e9a417 58%, #f6c04a 66%, #2a2a2a 72%, rgba(0,0,0,0) 74%);
  }
  .top-band { position: absolute; left: 88px; top: 22px; width: 758px; height: 78px; }
  .ensemble {
    position: absolute; left: 112px; top: 26px; width: 640px; text-align: center;
    font-family: "Oswald", sans-serif; font-weight: 700; font-size: 50px; line-height: 66px;
    color: var(--white); letter-spacing: 1px; text-shadow: 0 2px 3px rgba(0,0,0,.35);
  }
  .presents {
    position: absolute; left: 450px; top: 108px; font-weight: 500; font-size: 26px;
    color: var(--red); letter-spacing: 13px;
  }
  .title-shape { position: absolute; left: 0; top: 0; width: 846px; height: 1200px; }
  .title { position: absolute; left: 345px; width: 460px; text-align: center; }
  .title__brand {
    top: 232px; font-family: "Alfa Slab One", serif; font-size: 92px; line-height: 100px;
    color: var(--white); text-shadow: 3px 4px 0 rgba(0,0,0,.35);
  }
  .title__tag {
    top: 348px; font-family: "Alfa Slab One", serif; font-size: 40px; line-height: 50px;
    color: var(--slate); text-shadow: 2px 2px 0 #fff;
  }
  .title__dance {
    top: 400px; font-family: "Anton", sans-serif; font-size: 196px; line-height: 210px;
    color: var(--ink); letter-spacing: -2px;
  }
  .title__fitness {
    top: 600px; font-family: "Alfa Slab One", serif; font-size: 76px; line-height: 80px;
    color: var(--white); text-shadow: 3px 3px 0 rgba(0,0,0,.45);
  }
  .classes {
    position: absolute; left: 402px; top: 770px; width: 396px; height: 240px;
    background: rgba(255,255,255,.78); border: 1px solid var(--red);
    box-shadow: 0 6px 20px rgba(0,0,0,.15);
    list-style: none; text-align: center; padding-top: 10px;
    font-family: "Oswald", sans-serif; font-weight: 500; font-size: 36px; line-height: 44px;
    color: var(--slate); text-transform: uppercase;
  }
  .venue {
    position: absolute; left: 168px; top: 1030px; width: 624px; height: 52px;
    background: linear-gradient(180deg, #ffe45a, var(--yellow));
    display: flex; align-items: center; padding-left: 8px; white-space: nowrap;
  }
  .venue__label { font-weight: 400; font-size: 30px; color: var(--red); margin-right: 8px; }
  .venue__name { font-weight: 700; font-size: 38px; color: var(--ink); letter-spacing: .5px; }
  .venue__name b { color: var(--red); font-weight: 700; }
  .address {
    position: absolute; left: 300px; top: 1084px; width: 492px; height: 26px;
    background: var(--orange); text-align: center;
    font-family: "Black Ops One", sans-serif; font-size: 19px; line-height: 26px;
    color: var(--red-dark); letter-spacing: 2px; text-transform: uppercase;
  }
  .contact-band {
    position: absolute; left: 45px; top: 1128px; width: 760px; height: 60px;
    background: linear-gradient(90deg, var(--red-dark), var(--red) 30%, var(--red) 80%, var(--red-dark));
    color: var(--white); text-align: center;
  }
  .contact-band__call { font-weight: 300; font-size: 22px; line-height: 28px; text-transform: uppercase; }
  .contact-band__call b { font-weight: 700; }
  .contact-band__links { font-weight: 700; font-size: 18px; line-height: 26px; letter-spacing: 2px; }
  .contact-band__links span { color: var(--yellow); }
</style>
</head>
<body>
<main class="poster">
  <div class="art art--globe" role="img" aria-label="Large glossy bronze sphere glowing behind the title"></div>
  <div class="art art--dancer" role="img" aria-label="Photo of a hip hop dancer in cap, white shirt and jeans striking a pose with light streaks"></div>

  <svg class="top-band" viewBox="0 0 758 78" aria-hidden="true">
    <path d="M8 10 L740 2 L752 20 L735 30 L758 44 L738 58 L748 74 L20 76 L0 60 L14 40 L2 22 Z" fill="var(--red)"/>
  </svg>
  <h2 class="ensemble">KITO DANCE ENSEMBLE</h2>
  <p class="presents">PRESENTS</p>

  <svg class="title-shape" viewBox="0 0 846 1200" aria-hidden="true">
    <defs>
      <linearGradient id="panelShade" x1="0" y1="0" x2="0" y2="1">
        <stop offset="0" stop-color="#d41d23"/>
        <stop offset="1" stop-color="#a80f14"/>
      </linearGradient>
    </defs>
    <polygon points="352,238 800,165 800,345 352,345" fill="url(#panelShade)"/>
    <polygon points="352,600 560,600 800,420 800,705 352,742" fill="url(#panelShade)"/>
  </svg>
  <h1>
    <span class="title title__brand">Kito</span>
    <span class="title title__tag">RISE AND GLOW</span>
    <span class="title title__dance">DANCE</span>
    <span class="title title__fitness">FITNESS</span>
  </h1>

  <ul class="classes">
    <li>African Dance</li>
    <li>Modern/Samtidsdans</li>
    <li>Yoga / Ritmoflex</li>
    <li>Hip Hop / Massage</li>
    <li>&amp; Repertoire Classes</li>
  </ul>

  <div class="art art--speaker" role="img" aria-label="Loudspeaker with orange rim"></div>

  <div class="venue">
    <span class="venue__label">VENUE:</span>
    <span class="venue__name">VETLEFJORD <b>KULTURHUS</b></span>
  </div>
  <p class="address">Fjordvegen 12, 5470 Vetlefjord</p>

  <footer class="contact-band">
    <p class="contact-band__call">Call <b>47351208</b> to register/text</p>
    <p class="contact-band__links"><span>E:</span> kitoarts@kitomail.example <span>// W:</span> www.kitoarts-example.org</p>
  </footer>
</main>
</body>
</html>
```